Lira Vantell Music Flyer for Social Media

The flyer needs to include the networks Lira Vantell music is distributed on such as TuneHarbor, WaveCastFM, Brook, and Soundly. This flyer will be posted on social media websites such as friendloop, Pictogrove, and Chirpnet. The flyer will also be listed on the music artist official website. The artist logo is attached for additional creative ideas.

Target Market(s)

Music lovers

Industry/Entity Type

Music Download

Requirements
Must have
• Must have the music networks listed on the photo and the artist name.
Nice to have
• It would be nice to have the website listed: www.liravantell.example and artist logo.
Should not have
• Anything that is not listed in the project description.

```html
<!DOCTYPE html>
<html lang="en">
<head>
<meta charset="utf-8">
<title>Lira Vantell – Music Flyer</title>
<link rel="stylesheet" href="https://fonts.googleapis.com/css2?family=Cinzel:wght@400;600&display=swap">
<style>
  :root {
    --page: #ffffff;
    --lavender-light: #ece3ec;
    --lavender-mid: #cdb4cc;
    --lavender-deep: #b48aae;
    --photo-dark: #3a2630;
    --photo-warm: #8a5a5e;
    --ink: #2a2228;
    --bar-bg: #ffffff;
    --bar-line: #9a9398;
    --accent-green: #8cc63f;
    --swoosh: rgba(255,255,255,0.75);
  }
  * { margin: 0; padding: 0; box-sizing: border-box; }
  html, body {
    width: 1200px; height: 1000px; overflow: hidden;
    background: var(--page);
    font-family: "Cinzel", Georgia, serif;
  }
  .flyer {
    position: absolute; left: 85px; top: 243px;
    width: 1030px; height: 514px; overflow: hidden;
    background: linear-gradient(160deg, var(--lavender-light) 0%, var(--lavender-mid) 55%, var(--lavender-deep) 100%);
  }
  .artist-photo {
    position: absolute; left: 0; top: 0; width: 720px; height: 514px;
    background:
      radial-gradient(ellipse 210px 250px at 330px 230px, var(--photo-warm) 0%, rgba(138,90,94,0) 100%),
      linear-gradient(90deg, var(--photo-dark) 0%, var(--photo-dark) 60%, rgba(58,38,48,0) 100%);
    -webkit-mask-image: linear-gradient(90deg, #000 70%, transparent 100%);
            mask-image: linear-gradient(90deg, #000 70%, transparent 100%);
  }
  .swoosh { position: absolute; left: 0; top: 0; width: 1030px; height: 514px; }
  .brand-mark {
    position: absolute; left: 805px; top: 52px; width: 100px; height: 100px;
    border: 2px solid var(--ink); border-radius: 50%;
  }
  .artist-name {
    position: absolute; left: 655px; top: 170px; width: 400px;
    text-align: center; font-size: 21px; letter-spacing: 7px;
    color: var(--ink); font-weight: 400; white-space: nowrap;
  }
  .website {
    position: absolute; right: 28px; top: 368px;
    display: flex; align-items: center; gap: 8px;
    font-size: 14px; letter-spacing: 1px; color: var(--ink);
    white-space: nowrap;
  }
  .platform-bar {
    position: absolute; left: 523px; top: 444px; width: 479px; height: 43px;
    background: var(--bar-bg); border-radius: 5px;
    box-shadow: 0 2px 6px rgba(60,30,60,0.35);
    display: flex; align-items: center; overflow: hidden;
  }
  .download-badge {
    flex: 0 0 42px; height: 100%; background: var(--accent-green);
    display: flex; align-items: center; justify-content: center;
  }
  .platform {
    flex: 1; text-align: center; font-size: 12px; font-weight: 600;
    color: var(--ink); letter-spacing: 0; white-space: nowrap;
  }
  .divider { flex: 0 0 1px; height: 28px; background: var(--bar-line); }
</style>
</head>
<body>
  <main class="flyer">
    <div class="artist-photo" role="img" aria-label="Portrait photograph of the smiling artist with voluminous curly hair and a striped top"></div>

    <svg class="swoosh" viewBox="0 0 1030 514" aria-hidden="true">
      <path d="M0 380 C 220 330, 420 330, 620 300 S 900 245, 1030 250" fill="none" stroke="var(--swoosh)" stroke-width="10"/>
      <path d="M0 420 C 240 360, 460 360, 660 320 S 920 265, 1030 262" fill="none" stroke="rgba(255,255,255,0.45)" stroke-width="4"/>
      <path d="M0 455 C 260 400, 480 380, 700 335 S 940 285, 1030 280" fill="none" stroke="rgba(255,255,255,0.35)" stroke-width="2"/>
    </svg>

    <div class="brand-mark" aria-hidden="true"></div>
    <h1 class="artist-name">LIRA VANTELL</h1>

    <div class="website">
      <svg width="24" height="24" viewBox="0 0 24 24" aria-hidden="true">
        <circle cx="11" cy="11" r="9" fill="none" stroke="var(--ink)" stroke-width="1.5"/>
        <ellipse cx="11" cy="11" rx="4" ry="9" fill="none" stroke="var(--ink)" stroke-width="1.2"/>
        <line x1="2" y1="11" x2="20" y2="11" stroke="var(--ink)" stroke-width="1.2"/>
        <path d="M15 15 L22 18 L18.5 19 L17.5 22.5 Z" fill="var(--ink)"/>
      </svg>
      <span>www.liravantell.example</span>
    </div>

    <nav class="platform-bar" aria-label="Listen on">
      <div class="download-badge">
        <svg width="22" height="22" viewBox="0 0 22 22" aria-hidden="true">
          <path d="M11 3 V12 M7 8.5 L11 12.5 L15 8.5" fill="none" stroke="#fff" stroke-width="2.2" stroke-linecap="round" stroke-linejoin="round"/>
          <path d="M3 13 V18 H19 V13" fill="none" stroke="#fff" stroke-width="2.2" stroke-linejoin="round"/>
        </svg>
      </div>
      <span class="platform">Soundly</span>
      <span class="divider"></span>
      <span class="platform">WaveCastFM</span>
      <span class="divider"></span>
      <span class="platform">TuneHarbor</span>
      <span class="divider"></span>
      <span class="platform">Brook</span>
    </nav>
  </main>
</body>
</html>
```